Redesign start page for existing online shop

We are selling building material (chimneys and flue pipes) as well as fireplaces (stoves). For this online shop we need a new start page. The domain is kaminwelt-versand.de. Here you can see the current design. We want a smoother design with just one banner in the middle instead of the three in the first row. The look has to be more professional and trustworthy. You can therefore play with the colors. We want to try some different orange instead of our yellow / orange color. A few more things: - The phone number has to be bigger and more highlighted - So the 5 advantages at the top should be shown in a different way - New design for the products below - New footer

Target Market(s)

Germany and other countries in Europe.

Industry/Entity Type

Home Builder

Number of Pages Required

1 page

Font styles to use
Other font styles liked:
• Please se the font on our current site.

Colors
f78f20
f68d4c

Requirements
Must have
• - Clear design - Trustworthy look - All elements Which are now shown shoulderstand be still there after redesigning -
Nice to have
• - See the Following sites to have a clou about our wishes: glutvia.de warmbrio.de

```html
<!DOCTYPE html>
<html lang="de">
<head>
<meta charset="utf-8">
<title>Kaminwelt Versand – Startseite</title>
<link href="https://fonts.googleapis.com/css2?family=Open+Sans:wght@400;600;700&family=Montserrat:wght@500;600;700&family=Pacifico&display=swap" rel="stylesheet">
<style>
:root{
  --orange:#f5a524;
  --orange-dark:#e8901a;
  --cream:#fffaf0;
  --ink:#333333;
  --muted:#777777;
  --line:#e4e4e4;
  --grey-band:#ededed;
  --dark:#3a3a3a;
  --darker:#2d2d2d;
  --white:#ffffff;
}
*{box-sizing:border-box;margin:0;padding:0}
html,body{width:1200px;height:3448px;overflow:hidden}
body{font-family:"Open Sans",Arial,sans-serif;color:var(--ink);background:var(--white);font-size:13px}
.wrap{width:880px;margin:0 auto;position:relative}

/* top bar */
.topbar{height:24px;background:#2f2f2f;color:#ddd;font-size:9px}
.topbar .wrap{display:flex;align-items:center;height:24px;justify-content:space-between}
.pills{display:flex;gap:6px}
.pill{background:#fff;color:#333;border-radius:2px;padding:2px 8px;font-size:8px}
.rating{color:#fff}.rating b{color:var(--orange);letter-spacing:2px;font-size:11px}
.account{display:flex;gap:18px}

/* header */
.header{height:96px}
.header .wrap{display:flex;align-items:center;height:96px;justify-content:space-between}
.logo{display:flex;align-items:center;gap:10px}
.logo-mark{width:38px;height:38px;border-radius:50%;background:var(--orange)}
.logo-name{font-family:"Montserrat",sans-serif;font-weight:600;font-size:21px;line-height:22px;color:#555}
.contact{display:flex;align-items:center;gap:18px}
.phone{display:flex;align-items:center;gap:10px}
.phone-num{font-size:22px;font-weight:700;color:var(--orange)}
.phone-hours{font-size:9px;color:var(--muted)}
.seal{width:50px;height:50px;border-radius:50%;background:#222;border:3px solid #ddd}

/* nav */
.nav{height:30px;border-top:1px solid var(--line);border-bottom:1px solid var(--line)}
.nav .wrap{display:flex;align-items:center;height:28px;justify-content:space-between}
.menu{display:flex;gap:44px;font-size:12px;font-weight:600}
.search{width:230px;height:20px;border:1px solid #ddd;border-radius:10px;font-size:10px;color:#aaa;padding:3px 10px;position:relative}
.search::after{content:"";position:absolute;right:-1px;top:-1px;width:20px;height:20px;border-radius:50%;background:var(--orange)}

/* hero */
.hero{height:452px;position:relative;background:linear-gradient(180deg,#6b5646 0%,#8c7564 45%,#4e3f35 100%);color:#fff;text-align:center}
.hero h1{position:absolute;top:128px;width:100%;font-family:"Montserrat",sans-serif;font-size:27px;letter-spacing:2px;font-weight:700}
.hero p{position:absolute;top:170px;width:100%;font-size:12px}
.btn{display:inline-block;background:var(--orange);color:#fff;font-weight:700;border-radius:16px;font-size:11px;letter-spacing:1px;white-space:nowrap}
.hero .btn{position:absolute;top:222px;left:520px;width:160px;height:34px;line-height:34px}
.hero-arrow{position:absolute;top:205px;width:40px;height:40px;border-radius:50%;border:2px solid #fff;background:rgba(0,0,0,.2)}
.hero-arrow svg{margin-top:10px}
.dots{position:absolute;top:412px;left:580px;display:flex;gap:6px}
.dots i{width:10px;height:10px;border-radius:50%;background:#fff}

/* brands */
.brands{height:148px;background:var(--grey-band)}
.brands .wrap{display:flex;justify-content:space-between;align-items:center;height:148px}
.brand{font-family:"Montserrat",sans-serif;font-weight:700;font-size:17px;color:#555;width:110px;text-align:center}

/* advantages */
.advantages{height:411px;text-align:center}
.section-title{font-family:"Montserrat",sans-serif;font-weight:700;letter-spacing:2px}
.advantages .section-title{color:var(--orange);font-size:16px;padding-top:38px}
.mini-flame{width:34px;height:34px;border-radius:50%;border:2px solid #ddd;margin:18px auto 0}
.adv-row{display:flex;justify-content:space-between;width:880px;margin:28px auto 0}
.adv{width:220px}
.adv-box{width:166px;height:165px;border:2px solid var(--orange);margin:0 auto;display:flex;align-items:center;justify-content:center}
.adv-label{font-size:12px;letter-spacing:.5px;margin-top:20px;line-height:20px;white-space:nowrap}

/* how it works */
.how{height:453px;position:relative;background:linear-gradient(180deg,#f3ad3c 0%,#f5a524 60%,#ef9a1c 100%);color:#fff;text-align:center;margin-top:7px}
.how .section-title{font-size:25px;padding-top:42px}
.how .sub{font-size:11px;margin-top:6px}
.steps{position:absolute;top:116px;left:160px;width:880px;height:200px}
.step{position:absolute;width:220px;text-align:center;margin-left:-110px}
.step-photo{width:152px;height:152px;border-radius:50%;border:6px solid #fff;margin:0 auto;background:linear-gradient(135deg,#d9d9d9,#8a8a8a)}
.step-label{font-size:12px;font-weight:700;letter-spacing:.5px;margin-top:14px;line-height:16px}
.step-arrow{position:absolute;top:66px}
.cta-line{position:absolute;top:370px;left:248px;display:flex;align-items:center;gap:40px}
.cta-script{font-family:"Pacifico",cursive;font-size:24px}
.btn-outline{border:2px solid #fff;color:#fff;font-size:12px;font-weight:700;padding:8px 18px;letter-spacing:1px}

/* products */
.products{padding-top:35px;height:979px}
.grid{display:grid;grid-template-columns:repeat(4,220px);border-top:1px solid var(--line);border-left:1px solid var(--line)}
.card{height:338px;background:var(--cream);border-right:1px solid var(--line);border-bottom:1px solid var(--line);padding:18px 12px;overflow:hidden}
.card-img{height:180px;background:linear-gradient(180deg,#f2f2f2,#c9c9c9);border-radius:4px}
.card h3{font-family:"Montserrat",sans-serif;font-size:10.5px;color:var(--orange);margin-top:14px;letter-spacing:0;white-space:nowrap}
.card p{font-size:9px;line-height:14px;color:#555;margin-top:6px;height:56px;overflow:hidden}
.card-foot{display:flex;gap:6px;margin-top:8px}
.price{background:#222;color:#fff;font-size:9px;border-radius:3px;padding:4px 8px;white-space:nowrap}
.card .btn{font-size:9px;padding:4px 14px;border-radius:12px}

/* trust */
.trust{display:flex;justify-content:space-between;margin-top:66px}
.trust-box{width:430px;height:172px;display:flex;align-items:center;gap:26px;padding:0 28px}
.trust-box.grey{background:#eeeeee;border:1px solid #ddd}
.trust-box.white{border:2px solid #ddd}
.badge{flex:none;width:110px;height:110px;border-radius:50%;background:linear-gradient(135deg,#444,#111)}
.badge.square{border-radius:6px;background:linear-gradient(135deg,#f0f0f0,#cfcfcf)}
.trust-box p{font-size:11px;line-height:19px;color:#444}

/* payments */
.payments{text-align:center;height:188px;padding-top:8px}
.payments .section-title{font-size:25px;color:#222}
.pay-row{display:flex;justify-content:space-between;margin-top:20px}
.pay{width:104px;height:60px;border:1px solid #ccc;display:flex;align-items:center;justify-content:center;font-weight:700;font-size:11px;color:#333;text-align:center;line-height:13px}

/* seo text */
.seo{height:404px;background:var(--dark);color:#bbb}
.seo h2{font-family:"Montserrat",sans-serif;font-size:16px;color:var(--orange);padding-top:40px;line-height:22px}
.seo p{font-size:11px;line-height:22px;margin-top:14px}
.seo p b{color:#fff}
.seo .more{display:block;color:var(--orange);font-weight:700;font-size:11px;margin-top:24px}

/* footer */
.footer{height:256px;background:var(--darker);color:#bbb;font-size:11px}
.cols{display:flex;padding-top:34px}
.col h4{font-family:"Montserrat",sans-serif;color:var(--orange);font-size:15px;margin-bottom:12px}
.col.links{width:312px}
.col.consult{width:282px}
.links-list{display:grid;grid-template-columns:140px 140px;line-height:21px}
.col p{line-height:21px}
.footer-bottom{display:flex;align-items:center;gap:40px;margin-top:14px}
.social{display:flex;gap:12px}
.social i{width:32px;height:32px;border-radius:50%;background:#d0d0d0}
.copy{font-size:12px;letter-spacing:1px}
</style>
</head>
<body>

<div class="topbar">
  <div class="wrap">
    <div class="pills"><span class="pill">Sicher einkaufen ▾</span><span class="pill">Vorteile ▾</span><span class="pill">Beratung &amp; Kontakt ▾</span></div>
    <div class="rating"><b>★★★★★</b> Sehr Gut (4.80/5.00) ✓</div>
    <div class="account"><span>Mein Konto</span><span>Warenkorb</span></div>
  </div>
</div>

<header class="header">
  <div class="wrap">
    <div class="logo">
      <span class="logo-mark"></span>
      <span class="logo-name">KAMINWELT<br>VERSAND</span>
    </div>
    <div class="contact">
      <div class="phone">
        <svg width="26" height="26" viewBox="0 0 24 24"><path fill="#f5a524" d="M6.6 10.8a15 15 0 0 0 6.6 6.6l2.2-2.2a1 1 0 0 1 1-.25 11.4 11.4 0 0 0 3.6.57 1 1 0 0 1 1 1V20a1 1 0 0 1-1 1A17 17 0 0 1 3 4a1 1 0 0 1 1-1h3.5a1 1 0 0 1 1 1c0 1.25.2 2.45.57 3.57a1 1 0 0 1-.25 1z"/></svg>
        <div><div class="phone-num">08141 / 733 410 0</div><div class="phone-hours">Mo. - Fr. von 09:00 bis 18:00 Uhr</div></div>
      </div>
      <span class="seal"></span>
    </div>
  </div>
</header>

<nav class="nav">
  <div class="wrap">
    <div class="menu"><span>Online-Shop ▾</span><span>Service ▾</span><span>Standorte</span><span>FürHändler</span><span>Installateure</span></div>
    <div class="search">Suchbegriff oder Artikelnummer</div>
  </div>
</nav>

<section class="hero" role="img" aria-label="Wohnraum mit freistehendem Kamin, Holzdecke und Kronleuchter">
  <span class="hero-arrow" style="left:58px"><svg width="16" height="16" viewBox="0 0 16 16"><path d="M10 2 4 8l6 6" stroke="#fff" stroke-width="2" fill="none"/></svg></span>
  <h1>DEUTSCHE MARKENQUALITÄT</h1>
  <p>Alle Edelstahlschornsteine hergestellt in Deutschland mit 25 Jahren Garantie.</p>
  <span class="btn">JETZT ENTDECKEN</span>
  <span class="hero-arrow" style="right:58px"><svg width="16" height="16" viewBox="0 0 16 16"><path d="m6 2 6 6-6 6" stroke="#fff" stroke-width="2" fill="none"/></svg></span>
  <div class="dots"><i></i><i></i><i></i></div>
</section>

<section class="brands">
  <div class="wrap">
    <span class="brand">Nordwerk</span><span class="brand">Heizhaus</span><span class="brand">Thermalis</span><span class="brand">Calora</span><span class="brand">Wärmeberg</span>
  </div>
</section>

<section class="advantages">
  <div class="section-title">IHRE VORTEILE</div>
  <div class="mini-flame"></div>
  <div class="adv-row">
    <div class="adv">
      <div class="adv-box"><svg width="70" height="80" viewBox="0 0 70 80"><circle cx="35" cy="32" r="28" fill="#f5a524"/><path d="M20 62 14 78l11-5 6 7 4-16M50 62l6 16-11-5-6 7-4-16" fill="#f5a524"/><circle cx="35" cy="32" r="18" fill="none" stroke="#fff" stroke-width="2"/></svg></div>
      <div class="adv-label">DEUTSCHE MARKENQUALITÄT</div>
    </div>
    <div class="adv">
      <div class="adv-box"><svg width="70" height="70" viewBox="0 0 70 70"><circle cx="35" cy="35" r="32" fill="#f5a524"/><circle cx="35" cy="35" r="22" fill="none" stroke="#fff" stroke-width="2"/><text x="35" y="45" text-anchor="middle" font-size="28" font-weight="700" fill="#fff" font-family="Open Sans">€</text></svg></div>
      <div class="adv-label">BESTPREISGARANTIE</div>
    </div>
    <div class="adv">
      <div class="adv-box"><svg width="90" height="56" viewBox="0 0 90 56"><rect x="0" y="4" width="56" height="36" fill="#f5a524"/><path d="M58 14h18l12 14v12H58z" fill="#f5a524"/><circle cx="18" cy="46" r="8" fill="#f5a524" stroke="#fff" stroke-width="3"/><circle cx="72" cy="46" r="8" fill="#f5a524" stroke="#fff" stroke-width="3"/></svg></div>
      <div class="adv-label">SCHNELLE LIEFERUNG</div>
    </div>
    <div class="adv">
      <div class="adv-box"><svg width="90" height="56" viewBox="0 0 90 56"><rect x="0" y="4" width="56" height="36" fill="#f5a524"/><path d="M58 14h18l12 14v12H58z" fill="#f5a524"/><circle cx="18" cy="46" r="8" fill="#f5a524" stroke="#fff" stroke-width="3"/><circle cx="72" cy="46" r="8" fill="#f5a524" stroke="#fff" stroke-width="3"/><text x="28" y="28" text-anchor="middle" font-size="13" font-weight="700" font-style="italic" fill="#fff" font-family="Open Sans">FREE</text></svg></div>
      <div class="adv-label">VERSANDKOSTENFREI<br>AB € 300,- (DARUNTER € 5,90)</div>
    </div>
  </div>
</section>

<section class="how" role="img" aria-label="Orangefarbene Fläche mit angedeuteter Hausfassade im Hintergrund">
  <div class="section-title">SO FUNKTIONIERT'S</div>
  <div class="sub">In wenigen Schritten zum richtigen Angebot für Ihre Sanierung</div>
  <div class="steps">
    <div class="step" style="left:77px"><div class="step-photo" role="img" aria-label="Laptop bei der Dateneingabe"></div><div class="step-label">DATEN ONLINE EINGEBEN</div></div>
    <svg class="step-arrow" style="left:196px" width="14" height="20" viewBox="0 0 14 20"><path d="m2 2 8 8-8 8" stroke="#fff" stroke-width="3" fill="none"/></svg>
    <div class="step" style="left:323px"><div class="step-photo" role="img" aria-label="Aufmaß mit Plan und Lineal"></div><div class="step-label">AUFMAß UND BERATUNG<br>DURCH KUNDENBERATER</div></div>
    <svg class="step-arrow" style="left:437px" width="14" height="20" viewBox="0 0 14 20"><path d="m2 2 8 8-8 8" stroke="#fff" stroke-width="3" fill="none"/></svg>
    <div class="step" style="left:562px"><div class="step-photo" role="img" aria-label="Zahlung mit Karte"></div><div class="step-label">ANGEBOT VON ERFAHRENEN<br>HANDWERKERN</div></div>
    <svg class="step-arrow" style="left:676px" width="14" height="20" viewBox="0 0 14 20"><path d="m2 2 8 8-8 8" stroke="#fff" stroke-width="3" fill="none"/></svg>
    <div class="step" style="left:801px"><div class="step-photo" role="img" aria-label="Lastwagen bei der Auslieferung"></div><div class="step-label">AUSFÜHRUNG</div></div>
  </div>
  <div class="cta-line"><span class="cta-script">Jetzt unverbindlich eine Anfrage stellen!</span><span class="btn-outline">ANFRAGE STELLEN ›</span></div>
</section>

<section class="products">
  <div class="wrap">
    <div class="grid">
      <div class="card"><div class="card-img" role="img" aria-label="Schornsteinverlängerung aus Edelstahl"></div><h3>SCHORNSTEINVERLÄNGERUNG</h3><p>Kaminverlängerungen frei konfigurierbar nach Ihren Wunschmaßen und in Handarbeit nach höchsten Ansprüchen hergestellt.</p><div class="card-foot"><span class="price">ab € 63,00</span><span class="btn">JETZT ANSEHEN ›</span></div></div>
      <div class="card"><div class="card-img" role="img" aria-label="Schornsteinabdeckung aus Edelstahl"></div><h3>SCHORNSTEINABDECKUNG</h3><p>Kaminabdeckungen für alle Schornsteine individuell bestellen. Höchste Langlebigkeit und Qualität für Ihren Schornstein.</p><div class="card-foot"><span class="price">ab € 63,00</span><span class="btn">JETZT ANSEHEN ›</span></div></div>
      <div class="card"><div class="card-img" role="img" aria-label="Wanddurchführung mit Blende"></div><h3>WANDDURCHFÜHRUNG</h3><p>Wanddurchführungen für die sichere Durchführung von Abgasrohren durch Hauswände. Brandschutz auf höchstem Niveau.</p><div class="card-foot"><span class="price">ab € 63,00</span><span class="btn">JETZT ANSEHEN ›</span></div></div>
      <div class="card"><div class="card-img" role="img" aria-label="Schwarzes Ofenrohr mit Bogen"></div><h3>OFENROHR</h3><p>Ofenrohre in den Farben schwarz oder gussgrau in Premiumqualität direkt hier bestellen. Höchste Qualität für Ihre Sicherheit.</p><div class="card-foot"><span class="price">ab € 63,00</span><span class="btn">JETZT ANSEHEN ›</span></div></div>
      <div class="card"><div class="card-img" role="img" aria-label="Schornsteinverlängerung aus Edelstahl"></div><h3>SCHORNSTEINVERLÄNGERUNG</h3><p>Kaminverlängerungen frei konfigurierbar nach Ihren Wunschmaßen und in Handarbeit nach höchsten Ansprüchen hergestellt.</p><div class="card-foot"><span class="price">ab € 63,00</span><span class="btn">JETZT ANSEHEN ›</span></div></div>
      <div class="card"><div class="card-img" role="img" aria-label="Schornsteinabdeckung aus Edelstahl"></div><h3>SCHORNSTEINABDECKUNG</h3><p>Kaminabdeckungen für alle Schornsteine individuell bestellen. Höchste Langlebigkeit und Qualität für Ihren Schornstein.</p><div class="card-foot"><span class="price">ab € 63,00</span><span class="btn">JETZT ANSEHEN ›</span></div></div>
      <div class="card"><div class="card-img" role="img" aria-label="Wanddurchführung mit Blende"></div><h3>WANDDURCHFÜHRUNG</h3><p>Wanddurchführungen für die sichere Durchführung von Abgasrohren durch Hauswände. Brandschutz auf höchstem Niveau.</p><div class="card-foot"><span class="price">ab € 63,00</span><span class="btn">JETZT ANSEHEN ›</span></div></div>
      <div class="card"><div class="card-img" role="img" aria-label="Schwarzes Ofenrohr mit Bogen"></div><h3>OFENROHR</h3><p>Ofenrohre in den Farben schwarz oder gussgrau in Premiumqualität direkt hier bestellen. Höchste Qualität für Ihre Sicherheit.</p><div class="card-foot"><span class="price">ab € 63,00</span><span class="btn">JETZT ANSEHEN ›</span></div></div>
    </div>
    <div class="trust">
      <div class="trust-box grey"><span class="badge square"></span><p>Wir bieten ausschließlich Waren von deutschen Markenherstellern an. Unser gesamtes Sortiment wird von Branchenführern hergestellt und unterliegt ständigen Qualitätskontrollen. Für Ihre Sicherheit nur das Beste zum fairen Preis.</p></div>
      <div class="trust-box white"><span class="badge"></span><p>Um unserem Premiumanspruch und unserem Leistungsversprechen gerecht zu werden, erhalten Sie bei uns selbstverständlich auch 25 Jahre Garantie auf alle Edelstahlschornsteine und Edelstahlschornstein Bauteile.</p></div>
    </div>
  </div>
</section>

<section class="payments">
  <div class="wrap">
    <div class="section-title">ZAHLUNGSARTEN</div>
    <div class="pay-row">
      <span class="pay">Kartenzahlung</span><span class="pay">Vorkasse</span><span class="pay">Kreditkarte</span><span class="pay">Lastschrift</span><span class="pay">Sofortkarte</span><span class="pay">Wallet</span><span class="pay">Direkt-<br>überweisung</span>
    </div>
  </div>
</section>

<section class="seo">
  <div class="wrap">
    <h2>Edelstahlschornsteine, Schornsteinverlängerungen, Ofenrohre und Schornstein Zubehör – alles bei kaminwelt-versand.de günstig kaufen.</h2>
    <p>Kann ich einen Edelstahlschornstein im Internet kaufen? Diese Frage haben Sie sich bestimmt noch nie gestellt. Bei anderen Waren ist das eine Selbstverständlichkeit, aber bei einem <b>Edelstahlkamin</b> denkt man zunächst nicht ans <b>Onlineshopping</b>. Dabei gibt es schon seit einigen Jahren diverse Plattformen, die alles rund um das Thema <b>Edelstahlschornstein</b> anbieten. Allerdings betreiben diese Anbieter ihre Webshops nur nebenher. Dies spiegelt sich in der schlechten Benutzerfreundlichkeit und der teilweise stark veralteten Technik der Seiten wieder. Kaminwelt Versand ist hier einen neuen Weg gegangen. Das Ziel war es, einen Onlineshop für Edelstahlschornsteine und <b>Schornstein Zubehör</b> auf die Beine zu stellen, der nicht nur professionell und nach dem neuesten Stand der Technik aufgebaut ist, sondern Ihnen auch die Sicherheit und Usability bietet, die Sie von großen Onlineplattformen anderer Branchen gewohnt sind. Mit einer effizienten Organisation, moderner Technik und jahrelanger Erfahrung mit dem Produkt Edelstahlschornstein konnte dieser Anspruch erfüllt werden.</p>
    <span class="more">READ MORE</span>
  </div>
</section>

<footer class="footer">
  <div class="wrap">
    <div class="cols">
      <div class="col links">
        <h4>QUICK LINK</h4>
        <div class="links-list"><span>Häufige Fragen</span><span>Über uns</span><span>AGB</span><span>Widerruf</span><span>Lieferung &amp; Zahlung</span><span>Datenschutz</span><span>Impressum</span><span>Kontaktieren Sie uns</span><span>Blog</span><span>Glossar</span></div>
      </div>
      <div class="col consult">
        <h4>KOSTENLOSE BERATUNG</h4>
        <p>08141 / 733 410 0<br>Mo. - Fr. von 09:00 bis 18:00 Uhr<br><span style="color:var(--orange)">info@kaminwelt-versand.de</span></p>
      </div>
      <div class="col">
        <h4>ADDRESS</h4>
        <p>Lindenhofweg 7<br>80331 München<br>Deutschland</p>
        <p style="margin-top:10px">Kaminwelt-Versand<br>Durchschnittliche Bewertung: 4.71 (von 5)</p>
      </div>
    </div>
    <div class="footer-bottom">
      <div class="social"><i></i><i></i><i></i><i></i><i></i></div>
      <div class="copy">© 2011 - 2016 KAMINWELT-VERSAND.DE</div>
    </div>
  </div>
</footer>

</body>
</html>
```